Email Signature

We would like to have an email Signature designed.
We have an idea, and a logo that we would like to be make more professional in design and look.

```html
<!DOCTYPE html>
<html lang="en">
<head>
<meta charset="utf-8">
<title>Tenfold Advisory – Email Signature</title>
<link rel="stylesheet" href="https://fonts.googleapis.com/css2?family=Arimo:wght@400;700&family=Questrial&display=swap">
<style>
  :root {
    --signature-black: #0c0c0c;
    --parquet-dark: #1a1a1a;
    --parquet-mid: #3a3a3a;
    --brand-blue: #1f86d6;
    --brand-orange: #f0602a;
    --text-white: #ffffff;
  }
  html, body {
    margin: 0;
    padding: 0;
    width: 1200px;
    height: 329px;
    overflow: hidden;
    background: var(--signature-black);
  }
  .signature {
    position: relative;
    width: 1200px;
    height: 329px;
    background: var(--signature-black);
    overflow: hidden;
  }
  .parquet-texture {
    position: absolute;
    inset: 0;
    background: radial-gradient(ellipse 45% 90% at 50% 45%, var(--parquet-mid) 0%, var(--parquet-dark) 45%, var(--signature-black) 100%);
  }
  .brand {
    position: absolute;
    left: 86px;
    top: 138px;
    display: flex;
    align-items: center;
    gap: 16px;
  }
  .brand-dot {
    width: 46px;
    height: 46px;
    border-radius: 50%;
    background: var(--brand-orange);
  }
  .brand-name {
    font-family: "Questrial", sans-serif;
    font-size: 44px;
    color: var(--brand-blue);
    letter-spacing: 1px;
    white-space: nowrap;
  }
  .contact {
    position: absolute;
    left: 727px;
    top: 100px;
    color: var(--text-white);
  }
  .contact-person {
    margin: 0 0 16px;
    font-family: "Arimo", sans-serif;
    font-size: 22px;
    font-weight: 400;
    white-space: nowrap;
  }
  .contact-name {
    font-size: 29px;
    font-weight: 400;
    letter-spacing: -0.3px;
  }
  .contact-line {
    margin: 0 0 14px;
    font-family: "Questrial", sans-serif;
    font-size: 19px;
    letter-spacing: 0.6px;
    white-space: nowrap;
  }
  .contact-label-mobile { color: var(--brand-orange); }
  .contact-label-web { color: var(--brand-blue); }
</style>
</head>
<body>
  <div class="signature">
    <div class="parquet-texture" role="img" aria-label="Dark charcoal parquet wood floor texture"></div>

    <div class="brand">
      <span class="brand-dot"></span>
      <span class="brand-name">Tenfold Advisory</span>
    </div>

    <div class="contact">
      <p class="contact-person"><span class="contact-name">Sam Whitford</span>, Client Relations</p>
      <p class="contact-line"><span class="contact-label-mobile">M:</span> +61400 218 375</p>
      <p class="contact-line"><span class="contact-label-web">W:</span> www.tenfoldadvisory.com.au</p>
    </div>
  </div>
</body>
</html>
```